Inflatable Movie Screen company needs a Brochure Design for sales kit

We need a brochure as per attached sketch drawing which is to:
1)follow the sample layout
2) attached images must be used
3) to follow company corporate colors or suggest something professional and appropriate for the theme

Target Market(s)

Corporate and Community Clubs

Industry/Entity Type

Entertainment

Requirements
Must have
• Colors to be in line with corporate colors OR to suggest something appropriate.
Nice to have
• A unique concept
Should not have
• Too fanciful

```html
<!DOCTYPE html>
<html lang="en">
<head>
<meta charset="utf-8">
<title>Outdoor Movie Screening Brochure</title>
<link href="https://fonts.googleapis.com/css2?family=Cinzel:wght@400;600&family=Open+Sans:wght@300;400;600;700&family=Varela+Round&display=swap" rel="stylesheet">
<style>
  :root {
    --band: #8b8c8f;
    --band-light: #acacae;
    --ink: #8a8a8c;
    --ink-strong: #7c7d80;
    --pill: #d2d3d5;
    --ring: #e3e3e5;
    --paper: #ffffff;
    --backdrop: #ecebe7;
    --spine: #c9c9cb;
  }
  * { box-sizing: border-box; margin: 0; padding: 0; }
  html, body { width: 1200px; height: 1200px; overflow: hidden; }
  body { background: var(--backdrop); position: relative; font-family: "Open Sans", sans-serif; }

  .spread {
    position: absolute; left: 20px; top: 190px;
    width: 1240px; height: 877px;
    transform: scale(0.935); transform-origin: 0 0;
    box-shadow: 0 6px 20px rgba(0,0,0,0.12);
  }
  .page { position: absolute; top: 0; height: 877px; width: 620px; }
  .page--left { left: 0; background: linear-gradient(90deg, var(--paper) 0%, var(--paper) 45%, var(--spine) 100%); }
  .page--right { left: 620px; background: var(--paper); }

  .section-band {
    position: absolute; height: 42px; background: var(--band);
    color: #fff; font-family: "Cinzel", serif; font-size: 25px; font-weight: 400;
    letter-spacing: 0.5px; line-height: 42px; padding-left: 42px;
  }

  .reason { position: absolute; left: 0; width: 620px; }
  .reason__badge {
    position: absolute; left: 42px; width: 80px; height: 80px; border-radius: 50%;
    background: var(--band); border: 5px solid var(--ring);
    color: #fff; font-family: "Varela Round", sans-serif; font-size: 42px; font-weight: 700;
    display: flex; align-items: center; justify-content: center;
  }
  .reason__text { position: absolute; left: 148px; width: 460px; color: var(--ink); font-size: 17.5px; line-height: 24.5px; font-weight: 400; white-space: nowrap; }
  .reason__title { font-weight: 600; color: var(--ink-strong); font-size: 18px; }

  .photo {
    position: absolute; border-radius: 50%; background: var(--ring);
    display: flex; align-items: center; justify-content: center;
  }
  .photo__fill { border-radius: 50%; width: calc(100% - 26px); height: calc(100% - 26px); }
  .fill--night-park { background: radial-gradient(circle at 45% 40%, #3d3a5a 0%, #2a2740 55%, #1c2a1e 100%); }
  .fill--plaza { background: radial-gradient(circle at 50% 45%, #6a6070 0%, #3c3038 60%, #2a2226 100%); }
  .fill--campus { background: linear-gradient(180deg, #c9d2dc 0%, #8a96a4 45%, #2e3a38 100%); }
  .fill--lawn { background: radial-gradient(circle at 50% 30%, #2f4c7a 0%, #20345a 45%, #2c4a28 100%); }
  .fill--garden { background: radial-gradient(circle at 45% 45%, #4a7fa8 0%, #2a3e3a 40%, #161a16 100%); }

  .testimonial {
    position: absolute; left: 41px; top: 740px; width: 340px; white-space: nowrap;
    font-family: "Cinzel", serif; font-size: 13.5px; line-height: 19.5px; color: #9a9a9c; letter-spacing: 0.2px;
  }

  .expect-lead { position: absolute; left: 140px; width: 340px; top: 98px; text-align: center; font-weight: 600; font-size: 18px; color: var(--ink-strong); }
  .goal {
    position: absolute; height: 27px; border-radius: 14px;
    background: linear-gradient(180deg, #e2e2e4 0%, var(--pill) 100%);
    color: #fff; font-weight: 700; font-size: 17.5px; line-height: 27px; text-align: center;
  }
  .addons { position: absolute; left: 41px; top: 294px; width: 400px; color: var(--ink); font-size: 17.5px; line-height: 24.3px; }

  .offer {
    position: absolute; left: 42px; top: 686px; width: 536px; height: 149px;
    background: var(--band-light); color: #fff; font-size: 17.5px; line-height: 24.3px; padding: 14px 20px 0 21px;
  }
  .offer ul { list-style: none; }
  .offer li { position: relative; padding-left: 23px; }
  .offer li::before { content: ""; position: absolute; left: 2px; top: 8px; width: 10px; height: 10px; background: #fff; }
</style>
</head>
<body>
  <main class="spread">
    <section class="page page--left">
      <h2 class="section-band" style="left:0;top:41px;width:310px;">Why Choose Us ?</h2>

      <div class="reason" style="top:101px;">
        <div class="reason__badge" style="top:2px;">1</div>
        <p class="reason__text" style="top:0;"><span class="reason__title">We are pioneers in this field</span><br>We have hosted outdoor move screening since 2008.<br>Till date, we have completed xx more events.</p>
      </div>

      <div class="reason" style="top:215px;">
        <div class="reason__badge" style="top:3px;">2</div>
        <p class="reason__text" style="top:2px;"><span class="reason__title">We are able to screen Starlit movies</span><br>We have partnered the only film licence company<br>that has exclusive rights to screen Starlit movies<br>in DVD and other formats.</p>
      </div>

      <div class="reason" style="top:331px;">
        <div class="reason__badge" style="top:3px;">3</div>
        <p class="reason__text" style="top:1px;"><span class="reason__title">We provide high quality, weather-proof screens</span><br>Made from the same material as cinema screens,<br>our high quality PVC screens enhances images and<br>movies viewers of an intensive cinematic experience<br>if you are holding your event outdoors, don't .....<br>for our screen is weather-proof.</p>
      </div>

      <h2 class="section-band" style="left:0;top:498px;width:310px;">Our Clientele</h2>

      <div class="photo" style="left:328px;top:512px;width:250px;height:250px;">
        <div class="photo__fill fill--night-park" role="img" aria-label="Families on green lawn chairs watching an outdoor screen under a night sky"></div>
      </div>

      <p class="testimonial">"Enjoyed wateking &lt;move name&gt; with<br>my family. It was nice to get away<br>from the usual malls and bond<br>together. My kids loved it!"<br>- Mei Tan, housewife</p>
    </section>

    <section class="page page--right">
      <h2 class="section-band" style="left:155px;top:41px;width:310px;padding-left:48px;">What To Expect</h2>
      <p class="expect-lead">Are you planning an event to ....</p>

      <div class="goal" style="left:171px;top:134px;width:278px;">Create brand awareness</div>
      <div class="goal" style="left:171px;top:162px;width:278px;">Launch a new product</div>
      <div class="goal" style="left:116px;top:191px;width:387px;">Enhance team/ corporate branding</div>
      <div class="goal" style="left:171px;top:220px;width:278px;">Build community spirit</div>
      <div class="goal" style="left:171px;top:249px;width:278px;">Improve staff welfare</div>

      <p class="addons">Let us organise a more screening event for you!<br>your experience can be completed with the<br>following add-ons:<br>a. Popocorn<br>b. Catering<br>c. Themed/ fringe-activities</p>

      <div class="photo" style="left:407px;top:297px;width:170px;height:170px;">
        <div class="photo__fill fill--plaza" role="img" aria-label="Audience seated in an open plaza facing a lit screen at night"></div>
      </div>
      <div class="photo" style="left:42px;top:458px;width:166px;height:166px;">
        <div class="photo__fill fill--campus" role="img" aria-label="Crowd on a lawn beside a building watching a daytime screening"></div>
      </div>
      <div class="photo" style="left:245px;top:420px;width:200px;height:200px;">
        <div class="photo__fill fill--lawn" role="img" aria-label="Large crowd on a park lawn at dusk facing a glowing screen among trees"></div>
      </div>
      <div class="photo" style="left:448px;top:552px;width:172px;height:172px;">
        <div class="photo__fill fill--garden" role="img" aria-label="Bright blue screen glowing between dark garden trees at night"></div>
      </div>

      <h2 class="section-band" style="left:0;top:644px;width:310px;">Book Now</h2>
      <div class="offer">
        <p>Sign up for our 1 year package now!</p>
        <ul>
          <li>Get 8 movie screenings at 20% off!</li>
          <li>Your staff will also enjoy 20% discount when they quote your corporate code to engage for their personal parties/ events</li>
        </ul>
      </div>
    </section>
  </main>
</body>
</html>
```